Webdesign für Heilpraktiker
Toller, professioneller und netter Kontakt. Alle Vorgaben und Ideen wurden aufgegriffen und noch verbessert ! Das Ergebnis ist sehr, sehr gut !!
Zielgruppe
Ich bin Heilpraktiker und betreibe eine Naturheilpraxis mit den Schwerpunkten der traditionellen chinesischen Medizin (TCM). Da ganz besonders in der Philosophie (sogenannte 'Schule' des Pa Dun). Aber auch in der traditionellen Heilweise der TCM, wie Akupunktur, Heilkräutermedizin und weiteres.
Die Zielgruppe sind Menschen, die medizinische Hilfe benötigen. (Vom Kind bis zum älteren Menschen).
Aufgabenstellung
Es gibt ein Praxislogo, ein Foto von mir und ggf. ein Landschaftsbild. Ich dachte an fünf Hauptseiten mit Untergruppen. Am Ende sollte alles in Wordpress formatiert werden können, um es zu veröffentlichen.
Weitere Fotos zur Unterstützung der Themen kann ich natürlich gerne liefern.
Die Gestaltung ist nicht festgesetzt. Sollte aber seriös rüber kommen.

```html
<!DOCTYPE html>
<html lang="de">
<head>
<meta charset="utf-8">
<title>Naturheilpraxis Lorenz Albrecht</title>
<link href="https://fonts.googleapis.com/css2?family=Lato:wght@400;700;900&display=swap" rel="stylesheet">
<style>
:root{
  --gold:#d4a25c;
  --gold-btn:#e2b86f;
  --dark:#333033;
  --text:#3a3a3a;
  --muted:#8a8a8a;
  --line:#e3e3e3;
  --light:#f4f4f4;
  --footer:#3b3b3d;
}
*{box-sizing:border-box;margin:0;padding:0}
html,body{width:1200px;height:2856px;overflow:hidden;background:#fff}
body{position:relative;font-family:'Lato',sans-serif;color:var(--text)}
.abs{position:absolute}

/* hero */
.hero{left:0;top:0;width:1200px;height:446px;
  background:linear-gradient(180deg,#bfc9cf 0%,#aab59a 18%,#7f9a3e 45%,#6a8a2f 70%,#87793f 100%);
  clip-path:polygon(0 0,1200px 0,1200px 344px,1048px 446px,150px 446px,0 340px)}
.hero-title{left:0;width:1200px;top:205px;text-align:center;color:#fff;font-size:42px;line-height:49px;font-weight:400;text-shadow:0 1px 4px rgba(0,0,0,.25)}
.hero-title b{font-weight:900}
.brand{left:147px;top:28px;display:flex;align-items:center;gap:10px;font-size:17px;font-weight:700;color:#fff}
.brand-dot{width:22px;height:22px;border-radius:50%;background:var(--gold)}
.topbar{right:148px;top:10px;display:flex;gap:18px;font-size:12px;color:#fff;align-items:center}
.topbar span{display:flex;align-items:center;gap:7px}
.ico-circle{width:24px;height:24px;border-radius:50%;background:var(--gold);display:flex;align-items:center;justify-content:center}
.nav{right:148px;top:54px;display:flex;font-size:11.5px;font-weight:900;color:#111;text-transform:uppercase}
.nav a{padding:10px 13px;color:#111;text-decoration:none}
.nav a.active{background:var(--gold-btn);color:#fff;padding:10px 16px}

/* profile */
.profile{left:151px;top:513px;width:700px;height:259px;background:#f6f6f6;border:1px solid #e6e6e6;border-radius:4px}
.profile-head{left:151px;top:513px;width:700px;height:89px;background:var(--dark);border-radius:4px 4px 0 0;padding:15px 36px}
.profile-head h2{color:var(--gold);font-size:22px;letter-spacing:2px;font-weight:700}
.profile-head p{color:#fff;font-size:12.5px;line-height:15px;margin-top:6px}
.facts{left:188px;top:610px;list-style:none;font-size:13px}
.facts li{display:flex;align-items:center;gap:14px;height:30px}
.portrait{left:749px;top:486px;width:314px;height:314px;border-radius:50%;background:var(--gold);padding:12px}
.portrait div{width:100%;height:100%;border-radius:50%;background:radial-gradient(circle at 50% 40%,#b8b0ac,#5d636d 75%)}

/* sections */
.sec-h{font-size:16px;letter-spacing:2px;color:var(--gold);font-weight:700;text-transform:uppercase}
.photo{width:427px;height:231px}
.card-text{width:427px}
.card-text p{font-size:12.5px;line-height:20px;width:425px}
.card-text p.loose{line-height:23px}
.more{display:inline-block;margin-top:13px;margin-left:2px;font-size:13px;color:var(--gold);text-decoration:underline}

.help{left:0;top:1251px;width:1200px;height:451px;border:1px solid var(--line)}
.help-split{left:600px;top:1251px;width:1px;height:451px;background:var(--line)}
.help-intro{left:150px;top:1319px;width:410px;font-size:12.5px;line-height:19px;font-weight:700}
.help-list{left:150px;top:1380px;list-style:none;font-size:12.5px;line-height:18px}
.help-list li{display:flex;gap:14px;margin-bottom:12px;width:410px}
.help-list svg{flex:none;margin-top:3px}
.btn-more{left:151px;top:1623px;width:128px;height:39px;background:var(--gold-btn);border-radius:2px;font-size:13px;display:flex;align-items:center;justify-content:center;gap:8px;color:#222}

/* contact */
.contact{left:0;top:2218px;width:1200px;height:494px;background:var(--light)}
.form-h{left:684px;top:2290px;font-size:16px;font-weight:700;letter-spacing:2px;color:#222}
.field{left:685px;width:330px;height:35px;background:#fff;border:1px solid #e0e0e0;font-size:11px;color:var(--muted);padding:10px 16px}
.send{left:684px;top:2590px;width:331px;height:42px;background:var(--gold-btn);display:flex;align-items:center;justify-content:center;gap:10px;font-weight:700;letter-spacing:1px;font-size:14px;color:#333}

/* footer */
.footer{left:0;top:2712px;width:1200px;height:144px;background:var(--footer)}
.foot{font-size:12px;line-height:18px;color:#a9a9a9}
</style>
</head>
<body>

<div class="abs hero" role="img" aria-label="Grüne Berglandschaft mit Tälern unter hellem Himmel"></div>
<div class="abs brand"><div class="brand-dot"></div>Praxis Albrecht</div>
<div class="abs topbar">
  <span><span class="ico-circle"><svg width="12" height="12" viewBox="0 0 24 24" fill="none" stroke="#fff" stroke-width="2"><path d="M5 3h4l2 5-3 2a11 11 0 0 0 6 6l2-3 5 2v4a2 2 0 0 1-2 2A17 17 0 0 1 3 5a2 2 0 0 1 2-2"/></svg></span>0531 – 408 72 19</span>
  <span><span class="ico-circle"><svg width="12" height="12" viewBox="0 0 24 24" fill="none" stroke="#fff" stroke-width="2"><rect x="3" y="5" width="18" height="14"/><path d="M3 5l9 8 9-8"/></svg></span>post@praxis-albrecht-natur.de</span>
</div>
<nav class="abs nav">
  <a class="active">Startseite</a><a>Zu meiner Person</a><a>Wobei kann ich helfen</a><a>Der erste Besuch</a><a>Was ist das Pa Dun</a><a>Kontakt</a>
</nav>
<h1 class="abs hero-title"><b>Naturheilpraxis</b> des<br>Heilpraktiker Lorenz Albrecht</h1>

<div class="abs profile"></div>
<div class="abs profile-head">
  <h2>LORENZ ALBRECHT</h2>
  <p>Heilpraktiker und zertifizierter Therapeut der traditionellen chinesischen Medizin<br>(Berufsverband BVTN e.V.)</p>
</div>
<ul class="abs facts">
  <li><svg width="20" height="20" viewBox="0 0 20 20" fill="none" stroke="#333" stroke-width="1.6"><circle cx="10" cy="10" r="8.5"/><path d="M6 10l3 3 8-9" stroke="var(--gold)" stroke-width="2"/></svg>Jahrgang 1967</li>
  <li><svg width="20" height="20" viewBox="0 0 20 20" fill="none" stroke="#333" stroke-width="1.6"><circle cx="10" cy="10" r="8.5"/><path d="M6 10l3 3 8-9" stroke="var(--gold)" stroke-width="2"/></svg>Seit 2006 Heilpraktiker in Braunschweig</li>
  <li><svg width="20" height="20" viewBox="0 0 20 20" fill="none" stroke="#333" stroke-width="1.6"><circle cx="10" cy="10" r="8.5"/><path d="M6 10l3 3 8-9" stroke="var(--gold)" stroke-width="2"/></svg>Seit 2010 Gründer und Leiter des VLA Blutanalyselabors in Braunschweig</li>
  <li><svg width="20" height="20" viewBox="0 0 20 20" fill="none" stroke="#333" stroke-width="1.6"><circle cx="10" cy="10" r="8.5"/><path d="M6 10l3 3 8-9" stroke="var(--gold)" stroke-width="2"/></svg>Seit 2015 zertifizierter TCM Therapeut (Berufsverband BVTN e.V.)</li>
  <li><svg width="20" height="20" viewBox="0 0 20 20" fill="none" stroke="#333" stroke-width="1.6"><circle cx="10" cy="10" r="8.5"/><path d="M6 10l3 3 8-9" stroke="var(--gold)" stroke-width="2"/></svg>Beschäftigung mit der Pa Dun Philosophie (Schule) seit 1988</li>
</ul>
<div class="abs portrait" role="img" aria-label="Porträtfoto des Heilpraktikers"><div></div></div>

<h3 class="abs sec-h" style="left:150px;top:868px">Was mache ich</h3>
<div class="abs photo" style="left:150px;top:900px;background:linear-gradient(120deg,#e9f2f8,#a9c6dc 55%,#dfeaf3)" role="img" aria-label="Arzt mit medizinischen Symbolen auf digitaler Oberfläche"></div>
<div class="abs card-text" style="left:150px;top:1142px">
  <p>Seit vielen Jahrzehnten begeistere ich mich für die Themen der Medizin und die Wiederherstellung der Gesundheit.</p>
  <a class="more">Mehr...</a>
</div>

<h3 class="abs sec-h" style="left:622px;top:868px">Die Praxis</h3>
<div class="abs photo" style="left:622px;top:900px;background:linear-gradient(110deg,#e8e8e8,#b9b9b9 40%,#e9e2dc 75%,#d7c8bd)" role="img" aria-label="Mikroskop und Blutprobe im Labor"></div>
<div class="abs card-text" style="left:622px;top:1140px">
  <p class="loose">Seit 2012 besteht die Praxis, in der sich auch das VLA Blutanalyselabor befindet, im dritten Stock eines Wohn- und Geschäftshauses in der...</p>
  <a class="more">Mehr...</a>
</div>

<div class="abs help"></div>
<div class="abs help-split"></div>
<h3 class="abs sec-h" style="left:150px;top:1289px">Wobei kann ich helfen</h3>
<p class="abs help-intro">Der Schwerpunkt meiner Tätigkeit ist die Beseitigung und Linderung von chronischen Erkrankungen und deren Folgen. Hierzu zählen u.a.:</p>
<ul class="abs help-list">
  <li><svg width="16" height="12" viewBox="0 0 16 12" fill="none" stroke="var(--gold)" stroke-width="2"><path d="M1 6l4 4 10-9"/></svg>Der rheumatische Formenkreis / Erkrankungen die mit Entzündungen und Schmerzzuständen einhergehen</li>
  <li><svg width="16" height="12" viewBox="0 0 16 12" fill="none" stroke="var(--gold)" stroke-width="2"><path d="M1 6l4 4 10-9"/></svg>Magen- und Darmbeschwerden / Unverträglichkeiten bis hin zu allergischen Dispositionen</li>
  <li><svg width="16" height="12" viewBox="0 0 16 12" fill="none" stroke="var(--gold)" stroke-width="2"><path d="M1 6l4 4 10-9"/></svg>Diabetes / Stoffwechselstörungen</li>
  <li><svg width="16" height="12" viewBox="0 0 16 12" fill="none" stroke="var(--gold)" stroke-width="2"><path d="M1 6l4 4 10-9"/></svg>Chronische virale- und bakterielle Belastungen</li>
  <li><svg width="16" height="12" viewBox="0 0 16 12" fill="none" stroke="var(--gold)" stroke-width="2"><path d="M1 6l4 4 10-9"/></svg>Belastungen psychischer Natur / Erschöpfungszustände</li>
  <li><svg width="16" height="12" viewBox="0 0 16 12" fill="none" stroke="var(--gold)" stroke-width="2"><path d="M1 6l4 4 10-9"/></svg>Long Covid Belastungen</li>
</ul>
<div class="abs btn-more"><svg width="14" height="10" viewBox="0 0 14 10" fill="none" stroke="#222" stroke-width="1.4"><path d="M0 5h12M8 1l4 4-4 4"/></svg>Lern mehr</div>
<div class="abs" style="left:625px;top:1285px;width:75px;height:385px;background:linear-gradient(180deg,#fbeceb,#f7dedd,#fbeceb)" role="img" aria-label="Dekoratives Muster medizinischer Symbole"></div>
<div class="abs" style="left:1100px;top:1285px;width:75px;height:385px;background:linear-gradient(180deg,#fbeceb,#f7dedd,#fbeceb)" role="img" aria-label="Dekoratives Muster medizinischer Symbole"></div>
<div class="abs" style="left:722px;top:1340px;width:356px;height:230px;background:radial-gradient(ellipse at 50% 85%,#f2e6d4,#f5f0ee 55%,#fff 75%)" role="img" aria-label="Halbkreis aus medizinischen Symbolen um das Praxiszeichen"></div>

<h3 class="abs sec-h" style="left:150px;top:1762px">Der erste Besuch</h3>
<div class="abs photo" style="left:150px;top:1794px;background:linear-gradient(110deg,#6b6458,#d8dadc 40%,#f1f2f3 70%,#c9ccd1)" role="img" aria-label="Arzt schreibt Notizen auf ein Klemmbrett"></div>
<div class="abs card-text" style="left:150px;top:2035px">
  <p>Am Anfang steht eine einstündige Anamnese mit ausführlicher Interpretation ihrer bisherigen Untersuchungsergebnisse und Laborberichten. Gegebenfalls werden weitere Laboraufträge zur Diagnosesicherung und Verlaufskontrolle beauftragt.</p>
  <a class="more">Mehr...</a>
</div>

<h3 class="abs sec-h" style="left:622px;top:1762px">Was ist das Pa Dun</h3>
<div class="abs photo" style="left:622px;top:1794px;background:linear-gradient(180deg,#c7cfd3,#93a4b3 45%,#445f84 80%,#2e4566)" role="img" aria-label="Älterer Mann und Frau joggen am Seeufer"></div>
<div class="abs card-text" style="left:622px;top:2033px">
  <p class="loose">Das Pa Dun ist aus unserer heutigen Sicht ein Ratgeber für ein harmonisches und gesundes Sein, im Zusammenleben mit allen Lebensformen.</p>
  <a class="more">Mehr...</a>
</div>

<div class="abs contact"></div>
<div class="abs" style="left:155px;top:2312px;width:390px;height:300px;border-radius:50%;background:radial-gradient(circle,#e2e2e2,#ececec 60%,#f4f4f4 72%)" role="img" aria-label="Illustration eines Briefumschlags mit Papierflieger und E-Mail-Zeichen"></div>
<h3 class="abs form-h">SCHNELLER KONTAKT</h3>
<div class="abs field" style="top:2335px">Vollständiger Name</div>
<div class="abs field" style="top:2377px">Email</div>
<div class="abs field" style="top:2419px">Telefon</div>
<div class="abs field" style="top:2461px;height:120px">Ihre Anfrage</div>
<div class="abs send"><svg width="16" height="16" viewBox="0 0 24 24" fill="none" stroke="#333" stroke-width="1.6"><path d="M22 2L2 10l8 3 3 9z M10 13l12-11"/></svg>SENDEN</div>

<div class="abs footer"></div>
<div class="abs" style="left:155px;top:2760px;display:flex;align-items:center;gap:8px;font-size:13px;font-weight:700;color:#cfcfcf"><div style="width:14px;height:14px;border-radius:50%;background:var(--gold)"></div>Praxis Albrecht</div>
<svg class="abs" style="left:341px;top:2752px" width="14" height="17" viewBox="0 0 14 17"><path d="M7 0a6 6 0 0 1 6 6c0 4-6 11-6 11S1 10 1 6a6 6 0 0 1 6-6z" fill="var(--gold)"/><circle cx="7" cy="6" r="2.2" fill="var(--footer)"/></svg>
<p class="abs foot" style="left:366px;top:2752px">Lorenz Albrecht<br>Lindenhofweg 14<br>38102 Braunschweig</p>
<svg class="abs" style="left:599px;top:2755px" width="14" height="14" viewBox="0 0 24 24" fill="none" stroke="var(--gold)" stroke-width="2"><path d="M5 3h4l2 5-3 2a11 11 0 0 0 6 6l2-3 5 2v4a2 2 0 0 1-2 2A17 17 0 0 1 3 5a2 2 0 0 1 2-2"/></svg>
<p class="abs foot" style="left:623px;top:2752px">Telefon 0531 – 408 72 19</p>
<svg class="abs" style="left:598px;top:2782px" width="15" height="12" viewBox="0 0 24 18" fill="none" stroke="var(--gold)" stroke-width="2"><rect x="1" y="1" width="22" height="16"/><path d="M1 1l11 9 11-9"/></svg>
<p class="abs foot" style="left:623px;top:2779px">post@praxis-albrecht-natur.de</p>
<p class="abs foot" style="left:931px;top:2754px;line-height:23px">Impressum<br>Datenschutzerklärung</p>

</body>
</html>
```